Rings and things/plans. Wedding planning checklist design

We are a wedding videography start-up that's about to launch a chatterly campaign. We need a simple yet premium looking design to showcase a wedding planning checklist which we have written. The main focus of the design should be:

- On A4 pages
- Appeal to young engaged women
- Anyone at home can print it off and stick it onto a fridge
- Premium looking

The contents doesn't have to be on one piece of A4, the list can span more than one page. Also, it doesn't have to be traditional folded brochure style, a full A4 sized list is preferred. The design will potentially be used in further A4 brochure style blog posts. The written checklist and our company logo is attached for reference.

Target Market(s)

Young engaged woman

Industry/Entity Type

Wedding

Requirements
Must have
• Simple and premium feel.
Nice to have
• flexible design that can be reused in the future for blog posts.

```html
<!DOCTYPE html>
<html lang="en">
<head>
<meta charset="utf-8">
<title>Rings &amp; Things – One Week Checklist</title>
<link href="https://fonts.googleapis.com/css2?family=Oswald:wght@300;400&family=Arimo:wght@400;700&display=swap" rel="stylesheet">
<style>
  :root {
    --blush: #fde2d9;
    --blush-line: #f4d2c7;
    --ink: #4f4f4f;
    --ink-soft: #3a3a3a;
    --paper: #ffffff;
    --photo-light: #eeeae6;
    --photo-mid: #d9cfc6;
    --lace: #f8ebe6;
  }
  * { margin: 0; padding: 0; box-sizing: border-box; }
  html, body { width: 849px; height: 1200px; overflow: hidden; background: var(--paper); }
  .page { position: relative; width: 849px; height: 1200px; overflow: hidden; background: var(--paper); }

  .masthead {
    position: absolute; left: 0; top: 0; width: 849px; height: 61px;
    background: var(--blush);
    display: flex; justify-content: center; align-items: center;
  }
  .brand-name {
    font-family: "Oswald", sans-serif; font-weight: 300; font-size: 20px;
    line-height: 1; color: var(--ink-soft);
  }

  .hero-photo {
    position: absolute; left: 0; top: 61px; width: 849px; height: 345px;
    background: linear-gradient(100deg, var(--photo-mid) 0%, var(--photo-light) 30%, #f6f3f0 55%, var(--photo-light) 80%, #cfc6bd 100%);
  }
  .week-badge {
    position: absolute; left: 573px; top: 124px; width: 222px; height: 201px;
    background: rgba(255,255,255,.93); border: 3px solid var(--blush-line);
    display: flex; flex-direction: column; justify-content: center; align-items: center;
    font-family: "Oswald", sans-serif; font-weight: 300; font-size: 44px; line-height: 1.45;
    letter-spacing: 3px; color: var(--ink);
  }

  .lace-decor {
    position: absolute; left: 656px; top: 406px; width: 193px; height: 630px;
    background: linear-gradient(90deg, rgba(248,235,230,0) 0%, var(--lace) 45%, var(--lace) 100%);
  }

  .checklist { position: absolute; top: 0; left: 0; }
  .task { position: absolute; width: 270px; }
  .task .box {
    position: absolute; left: 0; top: 3px; width: 20px; height: 20px;
    border: 3px solid var(--blush-line); background: var(--paper);
  }
  .task h3 {
    margin-left: 33px; font-family: "Oswald", sans-serif; font-weight: 300;
    font-size: 20px; line-height: 28px; color: var(--ink-soft);
  }
  .task p {
    margin-left: 33px; margin-top: 6px; font-family: "Arimo", sans-serif;
    font-size: 10px; line-height: 14px; color: var(--ink-soft);
  }

  .footer {
    position: absolute; left: 0; top: 1036px; width: 849px; height: 164px;
    background: var(--blush);
    font-family: "Oswald", sans-serif; font-weight: 300; font-size: 21px; line-height: 35px; color: var(--ink);
  }
  .author { position: absolute; left: 51px; top: 38px; }
  .contact { position: absolute; right: 52px; top: 38px; text-align: right; }
</style>
</head>
<body>
<div class="page">
  <header class="masthead">
    <div class="brand-name">Rings &amp; Things</div>
  </header>

  <div class="hero-photo" role="img" aria-label="Photo of a bride and groom holding a bouquet of white roses"></div>
  <div class="week-badge"><span>ONE</span><span>WEEK</span></div>

  <div class="lace-decor" role="img" aria-label="Soft blush lace pattern decoration"></div>

  <section class="checklist">
    <div class="task" style="left:51px; top:446px;">
      <span class="box"></span>
      <h3>Wedding rehearsal</h3>
      <p>Don't forget to time all journeys</p>
    </div>
    <div class="task" style="left:51px; top:512px;">
      <span class="box"></span>
      <h3>Prepare emergency bride<br>and groom kits</h3>
      <p>These can include toothpaste, painkillers, sanitary pads, needle/safety pins, makeup, tissue, deodorant, nail glue, hair gel etc</p>
    </div>
    <div class="task" style="left:51px; top:640px;">
      <span class="box"></span>
      <h3>Assign people to pack up after<br>the wedding</h3>
      <p>Minimize stress on the day by delegating tasks beforehand</p>
    </div>

    <div class="task" style="left:480px; top:448px;">
      <span class="box"></span>
      <h3>Confirm final attendances</h3>
      <p>Follow up with your guests to make sure<br>there aren't any last minute cancellations</p>
    </div>
    <div class="task" style="left:480px; top:523px;">
      <span class="box"></span>
      <h3>Get nails done</h3>
      <p>Follow up with your guests to make sure there<br>aren't any last minute cancellations</p>
    </div>
    <div class="task" style="left:480px; top:598px;">
      <span class="box"></span>
      <h3>Pack for your honeymoon</h3>
      <p>Keep up the wedding buzz by not having to<br>stress about packing</p>
    </div>
  </section>

  <footer class="footer">
    <div class="author">Written by Mara Linton<br>Wedding Planner</div>
    <div class="contact">021.555.0148<br>maralinton@example.com</div>
  </footer>
</div>
</body>
</html>
```